Boutique Fitness Facility needs a new meal plan design that is as hot as our workouts!

We are about to host our 6 week Coral Tide program and we need to have a great looking meal plan handout created that we can give to all of our participants.

I have attached an example of our current full meal plan, for a reference only.

As in the example I've provided, I'd like to have certain areas color coded such as the proteins being Blue, Fats -yellow, Carbs - orange and veggies- green.

These colors will corollate to the Breakfast - snack - lunch - snack - Dinner graph that I've provided and would like to have added to the new handout.

I would like our logo placed at the top and beneath the logo have the text "Coral Tide Challenge"

The flyer should be of a summer influence in colors and design and
All text should be easy to read.

Thank you and I look forward to seeing your design!

```html
<!DOCTYPE html>
<html lang="en">
<head>
<meta charset="utf-8">
<title>Coral Tide Challenge – Meal Plan</title>
<link rel="stylesheet" href="https://fonts.googleapis.com/css2?family=Archivo+Black&family=Poppins:wght@400;500;600;700;800&display=swap">
<style>
:root{
  --ink:#0d0d0d;
  --cream:#fbf9ef;
  --yellow:#f6d310;
  --blue:#3f4fc4;
  --orange:#f2881e;
  --green:#4fb43a;
  --tip-green:#3aa62a;
  --white:#ffffff;
  --stage:#bdbdbd;
}
*{box-sizing:border-box;margin:0;padding:0}
html,body{width:847px;height:1200px;overflow:hidden}
body{background:var(--stage);font-family:"Poppins",sans-serif;position:relative}
.sheet{position:absolute;left:25px;top:82px;width:796px;height:1035px;background:var(--cream);overflow:hidden;box-shadow:0 4px 14px rgba(0,0,0,.25)}
.gym-backdrop{position:absolute;left:0;top:0;width:796px;height:600px;background:radial-gradient(ellipse at 50% 40%,#262626 0%,#111 55%,#050505 100%)}
.torn-edge{position:absolute;left:0;top:560px;width:796px;height:60px}
.brand{position:absolute;left:45px;top:48px;width:300px;text-align:center}
.brand-name{font-family:"Poppins",sans-serif;font-weight:800;font-size:50px;line-height:1;color:var(--yellow);letter-spacing:-1px;white-space:nowrap}
.brand-tag{margin-top:12px;font-size:10px;font-weight:600;letter-spacing:3px;color:var(--yellow);white-space:nowrap}
.divider{position:absolute;left:366px;top:48px;width:1px;height:84px;background:#555}
.title{position:absolute;left:388px;top:44px;width:370px;font-family:"Archivo Black",sans-serif;text-align:center;font-weight:400;white-space:nowrap}
.title-main{font-size:46px;line-height:1;color:var(--yellow)}
.title-sub{font-size:34px;line-height:1.1;color:var(--white);letter-spacing:1px}
.food-group{position:absolute;top:180px;height:272px;border:1.5px solid var(--c);border-top:none}
.food-group::before{content:"";position:absolute;left:0;top:0;width:100%;height:1.5px;background:var(--c)}
.group-tab{position:absolute;left:8px;right:14px;top:-14px;height:26px;background:var(--c);color:var(--white);font-weight:700;font-size:14px;text-align:center;line-height:26px;clip-path:polygon(8% 0,92% 0,100% 100%,0 100%)}
.group-fats .group-tab{color:var(--ink)}
.food-list{list-style:none;position:absolute;left:10px;top:26px;right:6px}
.food-list li{display:flex;align-items:flex-start;gap:6px;font-size:10px;line-height:1.15;color:var(--white);margin-bottom:8.5px}
.food-list li::before{content:"";flex:0 0 9px;height:9px;margin-top:1px;border-radius:50%;background:var(--c)}
.group-protein{--c:var(--blue);left:55px;width:150px}
.group-fats{--c:var(--yellow);left:236px;width:150px}
.group-carbs{--c:var(--orange);left:413px;width:153px}
.group-veg{--c:var(--green);left:601px;width:151px}
.group-veg .food-list li{margin-bottom:9px}
.note{position:absolute;left:53px;top:474px;display:flex;align-items:center;gap:14px;color:var(--white);font-size:15px;font-weight:500}
.note-pill{background:var(--white);color:var(--ink);font-weight:700;border-radius:8px;padding:2px 14px;font-size:15px}
.note span.arrow{color:var(--yellow);margin-right:6px}
.meal{position:absolute;top:538px;width:140px;height:140px}
.meal svg{position:absolute;inset:0}
.meal-label{position:absolute;inset:0;display:flex;align-items:center;justify-content:center;color:var(--white);font-weight:700;font-size:12.5px;padding-top:28px}
.meal-icon{position:absolute;left:50px;top:34px;width:40px;height:30px;border-radius:6px;background:rgba(246,211,16,.35)}
.meal-breakfast{left:50px}
.meal-lunch{left:326px}
.meal-dinner{left:612px}
.snack{position:absolute;top:568px;width:100px;text-align:center}
.snack-arrows{display:flex;justify-content:center;gap:6px;height:18px}
.snack-tag{margin:6px auto 0;width:86px;height:22px;line-height:22px;background:var(--green);color:var(--white);font-weight:700;font-size:12.5px;clip-path:polygon(10% 0,90% 0,100% 100%,0 100%)}
.snack-note{margin-top:8px;font-size:9.5px;font-weight:700;line-height:1.1;color:var(--ink)}
.snack-1{left:206px}
.snack-2{left:493px}
.fuel{position:absolute;left:52px;top:722px;font-family:"Archivo Black",sans-serif;font-weight:400;line-height:1}
.fuel-top{font-size:30px;color:var(--ink)}
.fuel-sub{font-size:20px;color:var(--yellow)}
.mission{position:absolute;left:268px;top:686px;width:528px;height:86px;background:var(--yellow);clip-path:polygon(2% 6%,20% 0,45% 5%,70% 1%,100% 4%,100% 96%,75% 100%,50% 95%,25% 100%,0 94%);padding:18px 16px 0 28px;font-size:13.5px;line-height:1.22;color:var(--ink)}
.tips{position:absolute;left:52px;top:792px;width:730px;display:flex}
.tip{flex:none;padding:0 12px;border-left:1px solid #e3e0d2;height:190px}
.tip:first-child{padding-left:0;border-left:none}
.tip-icon{width:30px;height:30px;border-radius:4px;background:#1b1b1b;margin-bottom:12px}
.tip h3{font-size:15px;font-weight:700;line-height:1.12;color:var(--tip-green);margin-bottom:8px}
.tip p{font-size:9.6px;line-height:1.2;color:var(--ink)}
.tip-1{width:122px}.tip-2{width:155px}.tip-3{width:150px}.tip-4{width:143px}.tip-5{width:160px}
</style>
</head>
<body>
<main class="sheet">
  <div class="gym-backdrop" role="img" aria-label="Dim photo of a gym with weight racks and equipment"></div>
  <svg class="torn-edge" viewBox="0 0 796 60" preserveAspectRatio="none" aria-hidden="true">
    <polygon fill="var(--cream)" points="0,22 30,18 55,24 90,16 130,23 170,17 210,25 250,19 290,22 330,15 370,23 410,18 450,24 490,16 530,22 570,17 610,24 650,18 690,23 730,16 770,22 796,18 796,60 0,60"/>
  </svg>

  <header>
    <div class="brand">
      <div class="brand-name">PeakForge</div>
      <div class="brand-tag">PERSONAL GROUP TRAINING</div>
    </div>
    <div class="divider"></div>
    <h1 class="title">
      <div class="title-main">CORAL TIDE</div>
      <div class="title-sub">CHALLENGE</div>
    </h1>
  </header>

  <section class="food-group group-protein">
    <div class="group-tab">PROTEIN</div>
    <ul class="food-list">
      <li>4-6 oz Chicken Breast</li>
      <li>4-6oz Turkey Breast</li>
      <li>4-6 oz Filet Mignon</li>
      <li>4-6 oz Flank Steak</li>
      <li>4-6 oz Salmon</li>
      <li>4-6 oz Tuna</li>
      <li>4-6 oz Cod</li>
      <li>4-6 oz Cottage Cheese</li>
      <li>4-6 oz Greek Yogurt</li>
      <li>4-6 oz Tofu</li>
      <li>3 -5 egg whites + 1 whole egg</li>
    </ul>
  </section>

  <section class="food-group group-fats">
    <div class="group-tab">FATS</div>
    <ul class="food-list">
      <li>¼ - ½ Avocado</li>
      <li>1 tbs Olive Oil</li>
      <li>1 small handful Almonds, Walnuts, Cashews</li>
    </ul>
  </section>

  <section class="food-group group-carbs">
    <div class="group-tab">CARBS</div>
    <ul class="food-list">
      <li>3 – 4oz Sweet Potato</li>
      <li>¼ - ½ cup White Rice</li>
      <li>¼ - ½ cup Quinoa</li>
      <li>¼ - ½ cup Oatmeal</li>
      <li>¾ cup Blueberries</li>
      <li>¾ cup Strawberries</li>
      <li>¾ cup Raspberries</li>
      <li>1 med. Apple</li>
      <li>1 small orange</li>
      <li>1 small grapefruit</li>
    </ul>
  </section>

  <section class="food-group group-veg">
    <div class="group-tab">VEGETABLES</div>
    <ul class="food-list">
      <li>1 Scoop Powdered Greens</li>
      <li>1 Cup Sautéed Spinach</li>
      <li>1 Cup Sautéed Kale, Broccoli</li>
      <li>1 Cup Sautéed Bell Pepper</li>
      <li>1 Cup Sautéed Carrots</li>
      <li>1 Cup Sautéed Zucchini</li>
    </ul>
  </section>

  <div class="note">
    <span class="note-pill">NOTE:</span>
    <span><span class="arrow">&lt;</span>150 lbs stick to smaller portions</span>
    <span><span class="arrow">&gt;</span>150 lbs stick to larger portions.</span>
  </div>

  <div class="meal meal-breakfast">
    <svg viewBox="0 0 140 140" aria-hidden="true">
      <circle cx="70" cy="70" r="57" fill="var(--ink)"/>
      <circle cx="70" cy="70" r="62" fill="none" stroke="var(--orange)" stroke-width="10" stroke-dasharray="130 260" transform="rotate(150 70 70)"/>
      <circle cx="70" cy="70" r="62" fill="none" stroke="var(--blue)" stroke-width="10" stroke-dasharray="130 260" transform="rotate(270 70 70)"/>
      <circle cx="70" cy="70" r="62" fill="none" stroke="var(--green)" stroke-width="10" stroke-dasharray="130 260" transform="rotate(30 70 70)"/>
      <g fill="var(--white)" stroke="var(--ink)" stroke-width="1.5">
        <circle cx="22" cy="38" r="6"/><circle cx="118" cy="38" r="6"/><circle cx="70" cy="132" r="6"/>
      </g>
      <g font-size="7" font-weight="700" font-family="Poppins,sans-serif" text-anchor="middle" fill="var(--ink)">
        <text x="22" y="40.5">1</text><text x="118" y="40.5">1</text><text x="70" y="134.5">1</text>
      </g>
    </svg>
    <div class="meal-icon" role="img" aria-label="Breakfast icon"></div>
    <div class="meal-label">BREAKFAST</div>
  </div>

  <div class="snack snack-1">
    <div class="snack-arrows"><svg width="70" height="18" viewBox="0 0 70 18" aria-hidden="true"><path d="M4 12 Q16 2 28 10" fill="none" stroke="var(--yellow)" stroke-width="3"/><path d="M25 5 L31 11 L23 13Z" fill="var(--yellow)"/><path d="M40 12 Q52 2 64 10" fill="none" stroke="var(--white)" stroke-width="3"/><path d="M61 5 L67 11 L59 13Z" fill="var(--white)"/></svg></div>
    <div class="snack-tag">SNACK</div>
    <div class="snack-note">1/2 PORTION<br>OF PROTEIN</div>
  </div>

  <div class="meal meal-lunch">
    <svg viewBox="0 0 140 140" aria-hidden="true">
      <circle cx="70" cy="70" r="57" fill="var(--ink)"/>
      <circle cx="70" cy="70" r="62" fill="none" stroke="var(--orange)" stroke-width="10" stroke-dasharray="130 260" transform="rotate(150 70 70)"/>
      <circle cx="70" cy="70" r="62" fill="none" stroke="var(--blue)" stroke-width="10" stroke-dasharray="130 260" transform="rotate(270 70 70)"/>
      <circle cx="70" cy="70" r="62" fill="none" stroke="var(--green)" stroke-width="10" stroke-dasharray="130 260" transform="rotate(30 70 70)"/>
      <g fill="var(--white)" stroke="var(--ink)" stroke-width="1.5">
        <circle cx="22" cy="38" r="6"/><circle cx="118" cy="38" r="6"/><circle cx="70" cy="132" r="6"/>
      </g>
      <g font-size="7" font-weight="700" font-family="Poppins,sans-serif" text-anchor="middle" fill="var(--ink)">
        <text x="22" y="40.5">1</text><text x="118" y="40.5">1</text><text x="70" y="134.5">1</text>
      </g>
    </svg>
    <div class="meal-icon" role="img" aria-label="Lunch plate icon"></div>
    <div class="meal-label">LUNCH</div>
  </div>

  <div class="snack snack-2">
    <div class="snack-arrows"><svg width="70" height="18" viewBox="0 0 70 18" aria-hidden="true"><path d="M4 12 Q16 2 28 10" fill="none" stroke="var(--yellow)" stroke-width="3"/><path d="M25 5 L31 11 L23 13Z" fill="var(--yellow)"/><path d="M40 12 Q52 2 64 10" fill="none" stroke="var(--white)" stroke-width="3"/><path d="M61 5 L67 11 L59 13Z" fill="var(--white)"/></svg></div>
    <div class="snack-tag">SNACK</div>
    <div class="snack-note">1/2 PORTION<br>OF PROTEIN</div>
  </div>

  <div class="meal meal-dinner">
    <svg viewBox="0 0 140 140" aria-hidden="true">
      <circle cx="70" cy="70" r="57" fill="var(--ink)"/>
      <circle cx="70" cy="70" r="62" fill="none" stroke="var(--yellow)" stroke-width="10" stroke-dasharray="130 260" transform="rotate(150 70 70)"/>
      <circle cx="70" cy="70" r="62" fill="none" stroke="var(--blue)" stroke-width="10" stroke-dasharray="130 260" transform="rotate(270 70 70)"/>
      <circle cx="70" cy="70" r="62" fill="none" stroke="var(--green)" stroke-width="10" stroke-dasharray="130 260" transform="rotate(30 70 70)"/>
      <g fill="var(--white)" stroke="var(--ink)" stroke-width="1.5">
        <circle cx="22" cy="38" r="6"/><circle cx="118" cy="38" r="6"/><circle cx="70" cy="132" r="6"/>
      </g>
      <g font-size="7" font-weight="700" font-family="Poppins,sans-serif" text-anchor="middle" fill="var(--ink)">
        <text x="22" y="40.5">1</text><text x="118" y="40.5">1</text><text x="70" y="134.5">1</text>
      </g>
    </svg>
    <div class="meal-icon" role="img" aria-label="Roast dinner icon"></div>
    <div class="meal-label">DINNER</div>
  </div>

  <h2 class="fuel">
    <div class="fuel-top">FUEL YOUR</div>
    <div class="fuel-sub">CORAL TIDE!</div>
  </h2>
  <p class="mission">This plan isn't about starving yourself - it's about sculpting a lean, toned physique by shredding fat while preserving muscle.<br>Here's how to maximize your results</p>

  <section class="tips">
    <article class="tip tip-1">
      <div class="tip-icon" role="img" aria-label="Person eating at a table icon"></div>
      <h3>Eat Like a Champion</h3>
      <p>Stick to this list as close as possible for maximum results, 7 Days A Week.</p>
    </article>
    <article class="tip tip-2">
      <div class="tip-icon" role="img" aria-label="Running figure icon"></div>
      <h3>Burn More Than You Consume</h3>
      <p>This is the golden rule! You need to burn more calories than you consume to create a deficit and force your body to tap into fat stores for energy.</p>
    </article>
    <article class="tip tip-3">
      <div class="tip-icon" role="img" aria-label="Sleeping in bed icon"></div>
      <h3>Maximize Sleep</h3>
      <p>When sleep-deprived, your body produces more ghrelin (hunger hormone) and less leptin (satiety hormone). Aim for 7-8 hours of quality sleep nightly.</p>
    </article>
    <article class="tip tip-4">
      <div class="tip-icon" role="img" aria-label="Protein foods icon"></div>
      <h3>Prioritize Protein</h3>
      <p>Protein helps build and maintain muscle mass, which is crucial for boosting metabolism and burning more calories at rest.</p>
    </article>
    <article class="tip tip-5">
      <div class="tip-icon" role="img" aria-label="Crown icon"></div>
      <h3>Consistency is King/Queen</h3>
      <p>Don't expect overnight results. Stick to your plan, track your progress, and celebrate small victories. Remember, slow and steady wins the shred race!</p>
    </article>
  </section>
</main>
</body>
</html>
```